Concert festival poster

Poster invitation for 40th party designed to look like a concert festival. Using the samples attached as a guide, looking for a colorful, creative and eye catching invite.
The event will be held over a weekend at a farm, with music food, friends and drinks.

Target Market(s)

Party guests, friends and family

Industry/Entity Type

Festival

Colors

Designer to choose colors to be used in the design.

Requirements
Must have
• Brellafest- Mark Telford's 40th festival
• Event date- 5-7th October 2018. Main event 6th October 2018 from 3pm-late
• Come anytime over the weekend- food, drinks and fun provided.
• Address is 412 Stony Creek Lane, Marulan NSW
• All welcome, including children
• Bring your own tent or let us know and we can arrange glamping tent set-up on site
• RSVP by 1 May 2018 to Kate at kate.anne.telford@mailbox-demo.com or Mark at mtelford@vantor-telford.com.au
• Will add extra information on event at later stage- see below for editable section.
Nice to have
• Editable section to add details, preferable at bottom of poster.

```html
<!DOCTYPE html>
<html lang="en">
<head>
<meta charset="utf-8">
<title>Brellafest – Mark Telford's 40th Festival</title>
<link rel="stylesheet" href="https://fonts.googleapis.com/css2?family=Bebas+Neue&family=Bangers&family=Montserrat:wght@400;600;700;800&display=swap">
<style>
  :root {
    --sky-top: #d6ebf4;
    --sky-bottom: #b3dce8;
    --green: #4f8a3a;
    --green-dark: #3c6f2b;
    --orange-light: #f39a2a;
    --orange-dark: #e2571c;
    --navy: #17303d;
    --white: #ffffff;
    --frame-sky: #c6e6f1;
    --field-light: #c3cf4a;
    --field-dark: #8fb53b;
    --wood-light: #e9b45a;
    --wood-dark: #b57a25;
    --photo-light: #eed6b4;
    --photo-red: #c8473a;
    --photo-blue: #4f72a8;
    --body-text: #1f2b33;
  }
  * { margin: 0; padding: 0; box-sizing: border-box; }
  html, body { width: 848px; height: 1200px; overflow: hidden; }
  body { font-family: "Montserrat", sans-serif; }

  .poster {
    position: relative;
    width: 848px;
    height: 1200px;
    overflow: hidden;
    background: linear-gradient(180deg, var(--sky-top) 0%, var(--sky-bottom) 100%);
  }

  .host-name {
    position: absolute;
    left: 126px;
    top: 158px;
    font-family: "Montserrat", sans-serif;
    font-weight: 800;
    font-size: 40px;
    line-height: 40px;
    color: var(--green);
  }
  .milestone {
    position: absolute;
    right: 128px;
    top: 134px;
    text-align: right;
    font-family: "Montserrat", sans-serif;
    font-weight: 800;
    color: var(--green);
  }
  .milestone-number { display: block; font-size: 64px; line-height: 64px; color: var(--green-dark); }
  .milestone-label { display: block; font-size: 40px; line-height: 40px; }

  .festival-title {
    position: absolute;
    left: 126px;
    top: 252px;
    width: 596px;
    height: 96px;
  }

  .frame {
    position: absolute;
    left: 128px;
    top: 444px;
    width: 592px;
    height: 510px;
    background: var(--white);
    padding: 13px;
  }
  .frame-scene {
    position: relative;
    width: 100%;
    height: 100%;
    background: var(--frame-sky);
    overflow: hidden;
  }
  .fields {
    position: absolute;
    left: 0; right: 0; bottom: 0;
    height: 150px;
    background: linear-gradient(180deg, var(--field-light) 0%, var(--field-dark) 100%);
  }

  .hosts-photo {
    position: absolute;
    left: 330px;
    top: 368px;
    width: 346px;
    height: 448px;
    background: linear-gradient(160deg, var(--photo-light) 0%, var(--photo-red) 55%, var(--photo-blue) 100%);
  }

  .address {
    position: absolute;
    left: 154px;
    top: 466px;
    font-family: "Bangers", cursive;
    font-size: 24px;
    line-height: 30px;
    letter-spacing: 0.5px;
    color: var(--navy);
  }

  .date-sign {
    position: absolute;
    left: 64px;
    top: 644px;
    width: 210px;
    height: 172px;
  }
  .date-sign-board {
    position: absolute;
    inset: 0;
    background: linear-gradient(180deg, var(--wood-light) 0%, var(--wood-dark) 100%);
    clip-path: polygon(4% 30%, 78% 14%, 100% 40%, 84% 70%, 10% 84%, 0 60%);
  }
  .date-sign-text {
    position: absolute;
    left: 46px;
    top: 58px;
    transform: rotate(-14deg);
    font-family: "Bangers", cursive;
    color: var(--white);
    text-align: center;
    letter-spacing: 1px;
  }
  .date-sign-range { display: block; font-size: 30px; line-height: 28px; }
  .date-sign-range sup { font-size: 16px; }
  .date-sign-month { display: block; font-size: 18px; line-height: 18px; }

  .main-event {
    position: absolute;
    left: 128px;
    width: 592px;
    top: 862px;
    text-align: center;
  }
  .main-event-date {
    display: block;
    font-family: "Bangers", cursive;
    font-size: 36px;
    letter-spacing: 1px;
    color: var(--white);
    text-shadow: 2px 2px 0 var(--navy);
  }
  .main-event-time {
    display: block;
    font-weight: 700;
    font-size: 16px;
    color: var(--navy);
  }

  .details {
    position: absolute;
    left: 0;
    width: 848px;
    top: 964px;
    text-align: center;
    font-size: 14px;
    line-height: 18.6px;
    font-weight: 400;
    color: var(--body-text);
  }
  .details strong { font-weight: 600; }
</style>
</head>
<body>
<main class="poster">
  <h1>
    <span class="host-name">Mark<br>Telford's</span>
    <span class="milestone">
      <span class="milestone-number">40th</span>
      <span class="milestone-label">Festival</span>
    </span>
    <svg class="festival-title" viewBox="0 0 596 96" aria-label="Brellafest">
      <defs>
        <linearGradient id="title-gradient" x1="0" y1="0" x2="0" y2="1">
          <stop offset="0" stop-color="#f39a2a"/>
          <stop offset="1" stop-color="#e2571c"/>
        </linearGradient>
      </defs>
      <text x="0" y="92" textLength="596" lengthAdjust="spacingAndGlyphs"
            font-family="Bebas Neue, sans-serif" font-size="126" fill="url(#title-gradient)">BRELLAFEST</text>
    </svg>
  </h1>

  <section class="frame">
    <div class="frame-scene">
      <div class="fields" role="img" aria-label="Illustrated rolling green farm fields with pine trees and windmills"></div>
    </div>
  </section>

  <div class="hosts-photo" role="img" aria-label="Photo of two smiling hosts in straw hats and country outfits"></div>

  <p class="address">412,<br>Stony Creek Lane,<br>Marulan<br>NSW</p>

  <div class="date-sign">
    <div class="date-sign-board" role="img" aria-label="Wooden arrow signpost"></div>
    <p class="date-sign-text">
      <span class="date-sign-range">5 – 7<sup>TH</sup></span>
      <span class="date-sign-month">OCTOBER 2018</span>
    </p>
  </div>

  <p class="main-event">
    <span class="main-event-date">MAIN EVENT 6TH OCTOBER 2018</span>
    <span class="main-event-time">from 3pm-late</span>
  </p>

  <section class="details">
    <p>Come anytime over the weekend - Food, drinks and fun provided</p>
    <p>All welcome, including children.</p>
    <p>Bring your own tent or let us know and we can arrange glamping tent set-up on site</p>
    <p>RSVP by 1 May 2018 to Kate at <strong>kate.anne.telford@mailbox-demo.com</strong></p>
    <p>or Mark at <strong>mtelford@vantor-telford.com.au</strong></p>
  </section>
</main>
</body>
</html>
```